Need to drive pregnant women to my 3d4d ultrasound studio where i provide 4d ultrasound with hyperalistic imaging and gender reveals

Industry/Entity Type

Healthcare

Font styles to use
Decorative
Script

Requirements
Must have
• My Company name Latido de Luna 4D. EVERYTHING HAS TO BE IN SPANISH
Nice to have
• SIMPLE AND NOT TOO BUSY
Should not have
• website

```html
<!DOCTYPE html>
<html lang="es">
<head>
<meta charset="utf-8">
<title>Latido de Luna 4D</title>
<link rel="stylesheet" href="https://fonts.googleapis.com/css2?family=Mr+Dafoe&family=Lobster&display=swap">
<style>
  :root {
    --page: #cfcfcf;
    --board: #000000;
    --ink: #ffffff;
    --rule: #3a3a3a;
    --amber-light: #d98a3a;
    --amber-dark: #5a2a08;
    --skin-light: #f0c4b4;
    --skin-dark: #8a5a4a;
    --screen: #0a0f16;
  }
  * { margin: 0; padding: 0; box-sizing: border-box; }
  html, body {
    width: 1200px;
    height: 1191px;
    overflow: hidden;
    background: var(--page);
  }
  .billboard {
    position: absolute;
    left: 20px;
    top: 426px;
    width: 1160px;
    height: 338px;
    background: var(--board);
    color: var(--ink);
  }
  .brand-name {
    position: absolute;
    left: 29px;
    top: 58px;
    width: 866px;
    font-family: "Mr Dafoe", cursive;
    font-weight: 400;
    font-size: 100px;
    line-height: 1;
    white-space: nowrap;
    text-align: center;
    word-spacing: 6px;
  }
  .title-rule {
    position: absolute;
    left: 50px;
    top: 168px;
    width: 850px;
    height: 1px;
    background: var(--rule);
  }
  .tagline {
    position: absolute;
    left: 50px;
    top: 180px;
    width: 830px;
    font-family: "Lobster", cursive;
    font-size: 37px;
    line-height: 51px;
    text-align: center;
    white-space: nowrap;
  }
  .scan-screen,
  .scan-thumb,
  .newborn-photo {
    position: absolute;
  }
  .scan-screen {
    left: 919px;
    top: 14px;
    width: 227px;
    height: 154px;
    background: radial-gradient(ellipse at 55% 55%, var(--amber-light) 0%, var(--amber-dark) 45%, var(--screen) 72%);
  }
  .scan-thumb {
    left: 920px;
    top: 196px;
    width: 98px;
    height: 127px;
    background: radial-gradient(ellipse at 55% 45%, var(--amber-light) 0%, var(--amber-dark) 100%);
  }
  .newborn-photo {
    left: 1033px;
    top: 196px;
    width: 113px;
    height: 127px;
    background: radial-gradient(ellipse at 50% 50%, var(--skin-light) 0%, var(--skin-dark) 100%);
  }
</style>
</head>
<body>
  <section class="billboard">
    <h1 class="brand-name">Latido de Luna 4D</h1>
    <div class="title-rule"></div>
    <p class="tagline">Ofrecemos Ultrasonido 4D Con Imágenes<br>Hiperrealistas Y Revelación De Género</p>
    <div class="scan-screen" role="img" aria-label="Pantalla de ecografía 4D en tonos ámbar"></div>
    <div class="scan-thumb" role="img" aria-label="Imagen de ecografía 4D de un bebé"></div>
    <div class="newborn-photo" role="img" aria-label="Fotografía de un recién nacido dormido"></div>
  </section>
</body>
</html>
```